Trifold brochure

Please design a new trifold color brochure. I've uploaded our very outdated brochure for info purposes. I've uploaded some pictures of some items we've made as examples. Use stock photos or our photos, your preference. Use our new logo that is attached.

```html
<!DOCTYPE html>
<html lang="en">
<head>
<meta charset="utf-8">
<title>Harlow Steelworks – Trifold Brochure</title>
<link href="https://fonts.googleapis.com/css2?family=Michroma&family=Mulish:wght@400;600;700&family=Oswald:wght@500&display=swap" rel="stylesheet">
<style>
:root{
  --navy:#1e3d7d;
  --navy-deep:#1a3670;
  --royal:#1f4fa8;
  --bright:#0d63b8;
  --band:#1a75d1;
  --logo-blue:#23409a;
  --white:#ffffff;
  --card-grey:#e9ecf3;
  --ink:#1f2530;
  --rule:#3a3f4a;
  --page:#eef0f3;
}
*{margin:0;padding:0;box-sizing:border-box}
html,body{width:1200px;height:2414px;overflow:hidden;background:var(--page)}
body{position:relative;font-family:"Mulish",Arial,sans-serif;color:var(--ink)}
.spread{position:absolute;left:30px;width:1140px;height:810px;overflow:hidden}
.spread--outside{top:382px;background:var(--navy)}
.spread--inside{top:1212px;background:var(--navy-deep)}
.abs{position:absolute}
.wordmark{font-family:"Michroma",sans-serif;line-height:1.05;letter-spacing:.5px;white-space:nowrap}
.mark-square{display:inline-block;vertical-align:middle;margin-right:10px;flex:none}

/* outside: back flap */
.panel-gallery{left:0;top:0;width:380px;height:810px}
.panel-gallery .mini-brand{left:48px;top:56px;width:150px;color:var(--white);font-size:9.5px;letter-spacing:0;display:flex;align-items:center}
.panel-gallery .mini-brand .mark-square{margin-right:6px}
.panel-gallery .mini-tag{left:210px;top:54px;color:var(--white);font-family:"Michroma",sans-serif;font-size:11px;line-height:1.4;white-space:nowrap}
.photo-circle{border-radius:50%;background:radial-gradient(circle at 50% 45%,#8a8f98 0%,#cfd3d9 45%,#ffffff 70%)}
.photo-plain{background:linear-gradient(#ffffff,#e8ebef)}
/* outside: back panel */
.panel-back{left:380px;top:0;width:380px;height:810px;text-align:center;color:var(--white)}
.panel-back .brand{left:0;right:0;top:92px;font-size:22px;display:flex;justify-content:center;align-items:center}
.address{left:0;right:0;top:585px;font-size:14px;line-height:1.35}
.address strong{font-size:15.5px;font-weight:700}
.social{left:0;right:0;top:696px;display:flex;justify-content:center;gap:14px}
.social span{width:20px;height:20px;border-radius:4px;background:var(--white);opacity:.85}
/* outside: cover */
.panel-cover{left:760px;top:0;width:380px;height:810px}
.cover-top{left:0;top:0;width:380px;height:350px;background:var(--white);text-align:center}
.cover-top .brand{position:absolute;left:0;right:0;top:80px;color:var(--logo-blue);font-size:25px;display:flex;justify-content:center;align-items:center}
.cover-top .custom{position:absolute;left:0;right:0;top:184px;font-family:"Michroma",sans-serif;font-size:20px}
.cover-top .metal{position:absolute;left:0;right:0;top:210px;font-family:"Michroma",sans-serif;font-size:48px;color:var(--royal);font-weight:700;letter-spacing:1px}
.cover-top .fab{position:absolute;left:0;right:0;top:272px;font-family:"Michroma",sans-serif;font-size:20px}
.values-band{left:0;top:350px;width:380px;height:38px;background:linear-gradient(90deg,var(--royal),var(--band) 55%,var(--royal));color:var(--white);font-family:"Oswald",sans-serif;font-size:18px;letter-spacing:.5px;display:flex;justify-content:center;align-items:center;gap:14px}
.cover-photo{left:0;top:388px;width:380px;height:270px;background:linear-gradient(160deg,#c8d6ea 0%,#7f9fc9 35%,#2c4d86 70%,#1a2f5c 100%);clip-path:polygon(0 0,100% 0,100% 64%,50% 100%,0 64%)}
.cover-url{left:0;right:0;top:740px;text-align:center;color:var(--white);font-size:15px}

/* inside */
.lower-band{left:0;top:440px;width:1140px;height:370px;background:var(--bright)}
.card{top:38px;width:315px;height:742px;clip-path:polygon(0 0,calc(100% - 40px) 0,100% 40px,100% 100%,0 100%)}
.card--mission{left:40px}
.card--products{left:418px;background:var(--card-grey)}
.card--contacts{left:785px}
.card-body{position:absolute;left:0;top:0;width:100%;height:404px;background:var(--white)}
.card-photo{position:absolute;left:0;top:404px;width:100%;height:338px;background:linear-gradient(150deg,#3c6fb9 0%,#224f98 50%,#10306a 100%)}
.tab{position:absolute;left:0;top:18px;height:36px;width:185px;background:var(--royal);color:var(--white);font-size:16px;font-weight:600;padding:8px 0 0 16px;clip-path:polygon(0 0,150px 0,100% 100%,0 100%)}
.mission-text{position:absolute;left:16px;top:76px;right:20px;font-size:19px;line-height:1.55}
.mission-text b{font-weight:700}
.products-intro{position:absolute;left:17px;top:75px;right:12px;font-size:12.5px;line-height:1.45}
.product-list{position:absolute;left:22px;top:160px;width:270px;list-style:none;display:grid;grid-template-columns:1fr 1fr;column-gap:0}
.product-list li{height:32px;padding:9px 0 0 10px;font-size:13px;border-bottom:1.5px solid var(--rule)}
.product-list li:nth-child(even){padding-left:16px}
.contacts-text{position:absolute;left:20px;top:93px;right:18px;font-size:12.5px;line-height:1.45}
.contacts-text p+p{margin-top:18px}
.contact-name{position:absolute;left:20px;top:282px;font-size:18px;font-weight:700;color:var(--navy-deep)}
.contact-lines{position:absolute;left:20px;top:312px;width:262px;list-style:none;color:var(--navy-deep)}
.contact-lines li{display:flex;align-items:center;gap:6px;font-size:13.5px;padding:4px 0 5px;border-bottom:1px solid #7a8193}
.contact-lines li:last-child{border-bottom:none;font-size:12.5px}
</style>
</head>
<body>

<section class="spread spread--outside" aria-label="Brochure outside">
  <div class="abs panel-gallery">
    <div class="abs mini-brand wordmark"><span class="mark-square" style="width:14px;height:14px;background:var(--white)"></span><span>HARLOW<br>STEELWORKS</span></div>
    <div class="abs mini-tag">Custom Metal<br>Fabrication</div>
    <div class="abs photo-circle" role="img" aria-label="Fabricated dust collector unit" style="left:95px;top:150px;width:200px;height:255px;border-radius:0 0 100px 100px"></div>
    <div class="abs photo-plain" role="img" aria-label="White steel hopper on a stand" style="left:105px;top:415px;width:175px;height:160px"></div>
    <div class="abs photo-circle" role="img" aria-label="Stainless steel transition housing" style="left:95px;top:584px;width:200px;height:200px"></div>
  </div>

  <div class="abs panel-back">
    <div class="abs brand wordmark"><span class="mark-square" style="width:22px;height:22px;background:var(--white)"></span><span>HARLOW<br>STEELWORKS</span></div>
    <div class="abs address">
      <strong>Harlow Steelworks, Inc.</strong><br>
      1427 Quarry Ln. Brookdale, VA 23199<br>
      Phone (555)-014-2290<br>
      www.harlowsteelworks.com
    </div>
    <div class="abs social" aria-label="Social links"><span></span><span></span><span></span></div>
  </div>

  <div class="abs panel-cover">
    <div class="abs cover-top">
      <div class="brand wordmark"><span class="mark-square" style="width:26px;height:26px;background:var(--logo-blue)"></span><span>HARLOW<br>STEELWORKS</span></div>
      <div class="custom">Custom</div>
      <div class="metal">METAL</div>
      <div class="fab">Fabrication</div>
    </div>
    <div class="abs values-band"><span>QUALITY</span><span>DEPENDABILITY</span><span>INTEGRITY</span></div>
    <div class="abs cover-photo" role="img" aria-label="Welder at work with sparks in a bright workshop"></div>
    <div class="abs cover-url">www.harlowsteelworks.com</div>
  </div>
</section>

<section class="spread spread--inside" aria-label="Brochure inside">
  <div class="abs lower-band"></div>

  <article class="abs card card--mission">
    <div class="card-body">
      <div class="tab">Our Mission</div>
      <p class="mission-text">We supply our customers <b>fabricated metal products</b> that are designed and produced with the highest quality, most competitive pricing, and the fastest lead-time<br>in the industry!</p>
    </div>
    <div class="card-photo" role="img" aria-label="Workers operating a shear and welding in the shop"></div>
  </article>

  <article class="abs card card--products">
    <div class="tab">Products</div>
    <p class="products-intro">Our products are as diverse as our customer base. Some of the products we specialize in are listed below…</p>
    <ul class="product-list">
      <li>Enclosures</li><li>Conveyors</li>
      <li>Platforms</li><li>Racks</li>
      <li>Stairs</li><li>Sheared Parts</li>
      <li>Guards</li><li>Welding</li>
      <li>Store Fixtures</li><li>Forming</li>
      <li>Baskets</li><li>Frames</li>
      <li>Pans</li><li>Modifications</li>
      <li>Duct Work</li><li>Channel</li>
      <li>Brackets</li><li>Panels</li>
      <li>Fittings</li><li>Cones</li>
      <li>Cladding</li><li>Discs</li>
      <li>Oxidizers</li><li>Shims</li>
      <li>Mixers</li><li>Covers</li>
      <li>Hoppers</li><li>Angles</li>
      <li>Ramps</li><li>Rails</li>
      <li>Carts</li><li>Clips</li>
      <li>Dryers</li><li>Transitions</li>
    </ul>
  </article>

  <article class="abs card card--contacts">
    <div class="card-body">
      <div class="tab">Contacts</div>
      <div class="contacts-text">
        <p>Our project managers have spent many years in the metal fabrication business. They are very knowledgeable and have vast experience in designing and producing items for different types of industries.</p>
        <p>Give them a call today and see how they can help you!</p>
      </div>
      <div class="contact-name">Harlow Steelworks, Inc.</div>
      <ul class="contact-lines">
        <li><svg width="10" height="12" viewBox="0 0 10 12"><path d="M5 0a4 4 0 0 1 4 4c0 3-4 8-4 8S1 7 1 4a4 4 0 0 1 4-4z" fill="none" stroke="#1a3670" stroke-width="1.3"/><circle cx="5" cy="4" r="1.3" fill="#1a3670"/></svg>1427 Quarry Ln. Brookdale, VA 23199</li>
        <li><svg width="10" height="10" viewBox="0 0 10 10"><path d="M2 0l2 2.5-1.2 1.3a6 6 0 0 0 3.4 3.4L7.5 6 10 8l-1.5 2C4 10 0 6 0 1.5z" fill="#1a3670"/></svg>(555)-014-2290</li>
        <li><svg width="10" height="10" viewBox="0 0 10 10"><circle cx="5" cy="5" r="4.3" fill="none" stroke="#1a3670" stroke-width="1.2"/><path d="M.7 5h8.6M5 .7c-2.5 2.6-2.5 6 0 8.6M5 .7c2.5 2.6 2.5 6 0 8.6" fill="none" stroke="#1a3670"/></svg>www.harlowsteelworks.com</li>
      </ul>
    </div>
    <div class="card-photo" role="img" aria-label="Welder joining steel frames with sparks while a colleague watches"></div>
  </article>
</section>

</body>
</html>
```